India March 15 Flyer

I would like a A4 Flyer made.
Very similair to attached file but the following changes
Name would be Explore Kerivan Weaving & Spice Journey

Cost $6995.00pp
16days fully escorted
Breakfast & Dinner included for 15days
Tour Departs Auckland 15th March 2015

Take out anything that is associated to Brisket Globe Voyages and it should be QMTrip Agents (attached) file for this.
Also no address just phone no's which is
09 573 8162
021736194
merel@qmtripagents.example.co.nz
QMTrip Agents Support Office:
Level 3, Pellor Finance Spire, 22-30 Quillane Rd,
Palmerston North 4493
Web:www.qmtripagents.example.co.nz
Under conditions take out Brisket Globe Voyages and put in QMTrip Agents and prices correct as at 20August 2014.
Under Conditions please change $400 deposit to $500 deposit pp.
Under Conditions: Price is Share Twin. Please advise if you want a single supplement cost.
I have attached a flyer that was done for me when i did the last tour. So this will give you an idea.
Also have attached the current itinerary that we will be doing for the March 2015 tour.
Hope this is enough information

Hello, Please do not forget to do the back of the flyer. dont put in itinerary but maybe a picture of the region that we are traveling and the Terms and Conditions which is so important. Thanks

I have noticed that the designs comming through dont have fully escorted by Merel Danforth which is a part of the brief with the flyer I included. Also return flights etc. Everything that was on the orginal flyer needs to include all of this except the Brisket Globe Voyages.

as this is a textile and culinary tour i would like to see pictures of textiles and food, as well as the normal pictures of India. I only seem to be getting elephant, taj extra but need to show the tour i am selling. Many thanks

Please re read the brief as i have made the required changes on this. IE: Price is now changed as well as some Terms and Conditions

• About Merel Danforth
• Pictures of Textiles and Culinerary as well as monuments

```html
<!DOCTYPE html>
<html lang="en">
<head>
<meta charset="utf-8">
<title>Explore Kerivan Weaving &amp; Spice Journey – Flyer</title>
<link href="https://fonts.googleapis.com/css2?family=Lato:wght@400;700;900&display=swap" rel="stylesheet">
<style>
:root{
  --bg:#2a2a2a;
  --green:#2fb34a;
  --green-dark:#1f8f36;
  --white:#ffffff;
  --ink:#222222;
  --orange:#f7a21b;
  --grey:#555555;
  --pale:#f3f9ee;
}
*{box-sizing:border-box;margin:0;padding:0}
html,body{width:1200px;height:800px;overflow:hidden;background:var(--bg);font-family:'Lato',sans-serif}
.canvas{position:relative;width:1200px;height:800px}
.page{position:absolute;top:32px;width:520px;height:736px;background:var(--green);overflow:hidden}
.page--back{left:50px}
.page--front{left:630px}

/* ---------- back page ---------- */
.back-panel{position:absolute;inset:14px;background:var(--white);border-radius:40px}
.tour-heading{position:absolute;left:26px;top:26px;color:var(--green);font-weight:900;font-size:11px;line-height:1.3}
.contact-block{position:absolute;right:22px;top:18px;color:var(--green);font-weight:700}
.contact-row{display:flex;align-items:center;gap:8px;font-size:15px;line-height:1.1}
.contact-row + .contact-row{margin-top:6px}
.contact-row svg{flex:none}
.contact-numbers{display:flex;flex-direction:column}
.contact-email{font-size:11px}
.about{position:absolute;left:26px;top:98px;width:235px;font-size:7px;line-height:1.35;color:var(--ink)}
.about strong{color:var(--green);font-weight:900}
.itinerary{position:absolute;left:22px;top:150px;width:240px;height:450px;background:var(--green);padding:8px 10px}
.itinerary h2{color:var(--white);font-size:11px;font-weight:900;text-align:center;margin-bottom:6px}
.itinerary-list{list-style:none;background:var(--pale);padding:8px 8px;height:410px;display:flex;flex-direction:column;justify-content:space-between}
.itinerary-list li{font-size:7.6px;line-height:1.3;color:var(--ink)}
.itinerary-list b{color:var(--green-dark)}
.gallery{position:absolute;right:22px;top:96px;width:226px;display:flex;flex-direction:column;gap:6px}
.gallery .photo{height:108px}
.photo--food{background:linear-gradient(135deg,#b8561c,#e7a13c 55%,#5d331a)}
.photo--textiles{background:linear-gradient(135deg,#b2224e,#6d2a7c 50%,#3a7a9a)}
.photo--market{background:linear-gradient(135deg,#d9474a,#f1c232 50%,#3b8e9b)}
.photo--monument{background:linear-gradient(180deg,#6aa6e0,#b9d4ee 55%,#7fa0b8)}
.terms{position:absolute;left:22px;top:606px;width:476px;font-size:5.8px;line-height:1.35;color:var(--grey)}
.terms strong{color:var(--orange);font-weight:900}
.office{position:absolute;left:150px;top:660px;font-size:7.5px;line-height:1.35;color:var(--ink);text-align:center}
.office strong{color:var(--green);font-weight:900}
.brand{font-weight:900;color:var(--ink);display:flex}
.brand--back{position:absolute;right:28px;top:672px;font-size:15px;flex-direction:column;align-items:flex-end}
.brand--back .agent{font-size:8px;color:var(--green);font-weight:700}

/* ---------- front page ---------- */
.hero{position:absolute;left:16px;top:16px;width:488px;height:430px;border-radius:34px 34px 0 0;background:linear-gradient(180deg,#2f4a2c 0%,#5f7d4c 45%,#a7b3a3 75%,#8a8f86 100%)}
.title-bubble{position:absolute;left:130px;top:98px;width:360px;height:126px}
.title-bubble svg{position:absolute;inset:0}
.title-text{position:absolute;inset:14px 14px 22px 14px;display:flex;flex-direction:column;justify-content:center;align-items:center;text-align:center;color:var(--orange);font-weight:900;font-size:25px;line-height:1.2}
.intro{position:absolute;left:20px;top:456px;width:290px;color:var(--white);font-size:10.5px;line-height:1.45}
.intro em{font-style:italic;font-weight:900}
.bottom-panel{position:absolute;left:16px;top:526px;width:488px;height:194px;background:var(--white);border-radius:0 0 34px 34px}
.front-contact{position:absolute;left:26px;top:556px;width:200px;color:var(--ink);font-size:12.5px;line-height:1.25}
.front-contact .icon{display:block;margin:0 auto 4px}
.front-contact .nums{text-align:center;font-size:14px}
.front-contact .web{margin-top:10px;white-space:nowrap}
.divider{position:absolute;left:236px;top:580px;width:2px;height:112px;background:var(--green)}
.brand--front{position:absolute;left:260px;top:630px;font-size:24px;flex-direction:column;align-items:flex-start}
.brand--front .agent{font-size:13px;color:var(--green);font-weight:700;align-self:flex-end}
.price-badge{position:absolute;right:12px;top:408px;width:204px;height:204px;border-radius:50%;background:var(--green);border:4px solid var(--white);color:var(--white);padding:28px 16px 0 32px}
.price-from{font-size:10px}
.price-amount{font-size:21px;font-weight:900}
.price-list{list-style:none;font-size:9px;line-height:1.22;margin-top:3px}
.price-list li::before{content:"\2022\00a0"}
.departs{position:absolute;right:26px;top:618px;color:var(--green);font-size:9px;font-style:italic;font-weight:700;transform:rotate(-2deg)}
</style>
</head>
<body>
<div class="canvas">

  <section class="page page--back">
    <div class="back-panel"></div>

    <header class="tour-heading">
      TEXTILE AND SHOPPING TOUR OF INDIA<br>
      16 Days / 15 Nights<br>
      Escorted by Merel Danforth
    </header>

    <div class="contact-block">
      <div class="contact-row">
        <svg width="22" height="18" viewBox="0 0 22 18" aria-hidden="true"><path d="M2 6c0-3 4-4 9-4s9 1 9 4v2h-5V6H7v2H2z" fill="#222"/><rect x="5" y="9" width="12" height="8" rx="2" fill="#222"/><circle cx="11" cy="13" r="2" fill="#fff"/></svg>
        <span class="contact-numbers"><span>09 573 8162</span><span>021736194</span></span>
      </div>
      <div class="contact-row contact-email">
        <svg width="18" height="13" viewBox="0 0 18 13" aria-hidden="true"><rect x="1" y="1" width="16" height="11" fill="none" stroke="#2fb34a" stroke-width="2"/><path d="M1 1l8 6 8-6" fill="none" stroke="#2fb34a" stroke-width="2"/></svg>
        <span>merel@qmtripagents.example.co.nz</span>
      </div>
    </div>

    <p class="about"><strong>About your Tour Manager Merel Danforth</strong><br>
      Merel has escorted many tours around India and has a passion for the culture and the people. Merel also has a business in New Zealand which deals with Rajasthani &amp; South India business's on a regular basis.</p>

    <div class="itinerary">
      <h2>Itinerary Overview</h2>
      <ul class="itinerary-list">
        <li><b>Day 1:</b> Arrive Delhi, transfer to hotel and rest.</li>
        <li><b>Day 2:</b> Delhi city tour with old bazaars and lunch.</li>
        <li><b>Day 3:</b> Train to Lucknow, evening walk through textile lanes.</li>
        <li><b>Day 4:</b> Lucknow embroidery workshop and local food tasting.</li>
        <li><b>Day 5:</b> Fly to Varanasi, evening ceremony on the river.</li>
        <li><b>Day 6:</b> Varanasi silk weavers visit, afternoon at leisure.</li>
        <li><b>Day 7:</b> Train to Agra, dinner at the hotel.</li>
        <li><b>Day 8:</b> Agra sunrise visit, marble inlay workshop tour.</li>
        <li><b>Day 9:</b> Drive to Jaipur, stop at the stepwell en route.</li>
        <li><b>Day 10:</b> Jaipur block printing class in Sanganer village.</li>
        <li><b>Day 11:</b> Jaipur forts, markets and a cooking lesson.</li>
        <li><b>Day 12:</b> Drive to Jodhpur, evening spice market walk.</li>
        <li><b>Day 13:</b> Jodhpur fort visit and tie dye studio.</li>
        <li><b>Day 14:</b> Drive to Udaipur via Ranakpur temple.</li>
        <li><b>Day 15:</b> Udaipur lake cruise and farewell dinner.</li>
        <li><b>Day 16:</b> Fly to Mumbai and connect home.</li>
      </ul>
    </div>

    <div class="gallery">
      <div class="photo photo--food" role="img" aria-label="Bowls of Indian curries, rice and breads"></div>
      <div class="photo photo--textiles" role="img" aria-label="Folded silk saris in pink, purple and blue"></div>
      <div class="photo photo--market" role="img" aria-label="Colourful market stall with bangles and fabrics"></div>
      <div class="photo photo--monument" role="img" aria-label="White marble mausoleum reflected in a long pool"></div>
    </div>

    <p class="terms"><strong>Terms &amp; Conditions:</strong> Price is share twin and correct as at 20 August 2014. Please advise if you want a single supplement cost. A $500 deposit per person is required to confirm your place. Final payment is due 60 days before departure. Prices may change with currency, fuel and taxes. Travel insurance is strongly advised. Cancellation fees apply. Itinerary may vary due to local conditions.</p>

    <p class="office"><strong>QMTrip Agents Support Office:</strong><br>
      Level 3, Pellor Finance Spire, 22-30 Quillane Rd,<br>
      Palmerston North 4493</p>

    <div class="brand brand--back"><span class="brand-name">QMTrip Agents</span><span class="agent">Merel Danforth</span></div>
  </section>

  <section class="page page--front">
    <div class="hero" role="img" aria-label="Monks in orange robes with yellow umbrellas walking down a tree-lined avenue"></div>

    <div class="title-bubble">
      <svg viewBox="0 0 360 126" width="360" height="126" aria-hidden="true"><path d="M24 0H336a24 24 0 0 1 24 24V104l6 22-30-14H24A24 24 0 0 1 0 88V24A24 24 0 0 1 24 0z" fill="#2fb34a"/></svg>
      <h1 class="title-text"><span>Explore Kerivan</span><span>Weaving &amp; Spice Journey</span></h1>
    </div>

    <p class="intro"><em>India</em> is one the most captivating countries on earth - from it's rich culture to breathing scenery. A trip to <em>India</em> will create memories to last you a life time</p>

    <div class="bottom-panel"></div>

    <div class="price-badge">
      <div class="price-from">from <span class="price-amount">$6995.00pp</span></div>
      <ul class="price-list">
        <li>16 days fully escorted</li>
        <li>Breakfast &amp; Dinner included for 15days</li>
        <li>Airfares Auckland to Delhi/Mumbai to Auckland Direct</li>
        <li>All assistance and transfers</li>
        <li>All current taxes</li>
      </ul>
    </div>
    <p class="departs">Tour Departs Auckland 15th March 2015</p>

    <div class="front-contact">
      <svg class="icon" width="22" height="18" viewBox="0 0 22 18" aria-hidden="true"><path d="M2 6c0-3 4-4 9-4s9 1 9 4v2h-5V6H7v2H2z" fill="#222"/><rect x="5" y="9" width="12" height="8" rx="2" fill="#222"/><circle cx="11" cy="13" r="2" fill="#fff"/></svg>
      <div class="nums">09 573 8162<br>021736194</div>
      <svg class="icon" width="18" height="13" viewBox="0 0 18 13" aria-hidden="true" style="margin-top:4px"><rect x="1" y="1" width="16" height="11" fill="#222"/><path d="M1 1l8 6 8-6" fill="none" stroke="#fff" stroke-width="1.5"/></svg>
      <div class="web">merel@qmtripagents.example.co.nz<br>www.qmtripagents.example.co.nz</div>
    </div>

    <div class="divider"></div>

    <div class="brand brand--front"><span class="brand-name">QMTrip Agents</span><span class="agent">Merel Danforth</span></div>
  </section>

</div>
</body>
</html>
```